Dog training that every member of the family can use. Humane safe and effective

Starting my own dog training business I would like a pic/drawing of human dog bonding, perhaps a paw in a human hand. Because I deal with all families/people I don't want a specific gender/age to be recognized. Also, to I would like it colorful to stand out since it is a big advertising tool for me. Paw prints included may be a nice feature.

Target Market(s)

People that are looking for a positive reinforcement dog trainer

Industry/Entity Type

Dog Training

Contact Information for Business Card

Vibrantly colored/eye catching business card.
Under Business name: "Helping build an everlasting bond"
Besides business name, Also Include:
place for my name
that I'm Owner/Trainer
email
phone #
web
Services provided:
private lessons
basic pet etiquette
behavior modification

Font styles to use
Other font styles liked:
• Lobster

Requirements
Must have
• paw prints, human hand shaking dogs paw (happy dog/panting)
Nice to have
• colors that attract the eye but not too busy

```html
<!DOCTYPE html>
<html lang="en">
<head>
<meta charset="utf-8">
<title>Tailwise Companions – Business Card</title>
<link rel="stylesheet" href="https://fonts.googleapis.com/css2?family=Lobster&family=Mulish:wght@600;700;800&display=swap">
<style>
  :root {
    --backdrop: #000000;
    --card-white: #f4f4f4;
    --pink: #cf2560;
    --green: #6db431;
    --ink: #231f20;
    --white: #ffffff;
  }
  * { margin: 0; padding: 0; box-sizing: border-box; }
  html, body { width: 1200px; height: 999px; overflow: hidden; background: var(--backdrop); }
  .canvas { position: relative; width: 1200px; height: 999px; }
  .card {
    position: absolute; left: 75px; top: 199px; width: 1050px; height: 599px;
    background: radial-gradient(circle at 25% 50%, #ffffff 0%, var(--card-white) 70%, #e2e2e2 100%);
    overflow: hidden;
  }
  .card-shapes { position: absolute; inset: 0; }
  .script { font-family: "Lobster", cursive; }
  .sans { font-family: "Mulish", sans-serif; }
  .abs { position: absolute; white-space: nowrap; }

  .brand-disc { position: absolute; left: 135px; top: 130px; width: 200px; height: 200px; border-radius: 50%;
    background: var(--pink); }
  .brand-name { left: 0; width: 470px; top: 360px; text-align: center; font-size: 34px; color: var(--pink); }

  .person-name { right: 115px; top: 72px; font-size: 46px; color: var(--white); }
  .person-role { right: 113px; top: 128px; font-size: 27px; font-weight: 700; color: var(--white); }
  .hand-mark { position: absolute; left: 955px; top: 66px; width: 76px; height: 84px; border-radius: 36px 36px 28px 28px;
    background: var(--ink); }

  .contact { right: 112px; font-weight: 700; color: var(--white); }
  .contact-phone { top: 290px; font-size: 29px; }
  .contact-email { top: 351px; font-size: 29px; }
  .contact-web { top: 414px; font-size: 22px; }
  .contact-icon { position: absolute; left: 969px; width: 46px; height: 46px; }

  .services-label { right: 30px; top: 523px; font-size: 17px; color: var(--white); }
  .services-list { right: 30px; top: 546px; font-size: 22px; color: var(--white); }
</style>
</head>
<body>
<main class="canvas">
  <section class="card">
    <svg class="card-shapes" width="1050" height="599" viewBox="0 0 1050 599" aria-hidden="true">
      <path d="M380,0 C450,80 490,230 470,350 C462,420 458,470 452,503 L1050,503 L1050,0 Z" fill="var(--pink)"/>
      <path d="M452,503 C440,550 432,575 425,599 L1050,599 L1050,503 Z" fill="var(--green)"/>
    </svg>

    <div class="brand-disc" aria-hidden="true"></div>
    <div class="abs script brand-name">Tailwise Companions, LLC</div>

    <div class="abs script person-name">Maren Ashcroft</div>
    <div class="abs sans person-role">Owner/Trainer</div>
    <div class="hand-mark" role="img" aria-label="Illustration of a hand with a paw print"></div>

    <div class="abs sans contact contact-phone">555-014-2236</div>
    <svg class="contact-icon" style="top:286px" viewBox="0 0 46 46" aria-hidden="true">
      <circle cx="23" cy="23" r="23" fill="var(--ink)"/>
      <path d="M16 12c2-1 3 0 4 2l1 3c0 1-1 2-2 3 1 3 3 5 6 6 1-1 2-2 3-2l3 1c2 1 3 2 2 4-1 2-3 3-5 3-8-1-14-7-15-15 0-2 1-4 3-5z" fill="var(--card-white)"/>
    </svg>

    <div class="abs sans contact contact-email">maren.ashcroft@example.net</div>
    <svg class="contact-icon" style="top:347px" viewBox="0 0 46 46" aria-hidden="true">
      <circle cx="23" cy="23" r="23" fill="var(--ink)"/>
      <rect x="12" y="15" width="22" height="16" fill="none" stroke="var(--card-white)" stroke-width="2"/>
      <path d="M12 15l11 9 11-9" fill="none" stroke="var(--card-white)" stroke-width="2"/>
    </svg>

    <div class="abs sans contact contact-web">marenashcroft.example.com/tailwise</div>
    <svg class="contact-icon" style="top:404px" viewBox="0 0 46 46" aria-hidden="true">
      <circle cx="23" cy="23" r="23" fill="var(--ink)"/>
      <text x="23" y="28" text-anchor="middle" font-family="Mulish, sans-serif" font-weight="800" font-size="13" fill="var(--card-white)">www</text>
    </svg>

    <div class="abs script services-label">Services Provided</div>
    <div class="abs script services-list">Private Lessons | Basic Pet Etiquette | Behavior Modification</div>
  </section>
</main>
</body>
</html>
```